Craft Instant Coffee Box Packaging design

We need packaging designed for our craft instant coffee. Needs to be simple yet eye-catching. We are looking to package instant coffee sachets inside a cigarette style box. Front of box must make it clear that it is instant coffee and show contents - 7 pack / 21g net as well as Drift Willow Roasters Co. which is the company name. We'd prefer the instant coffee be the focal point rather than the company name. The rear will have 'ingredients', company address and barcode. Sides should either state contents such as 'Instant Coffee' or company name.

Font styles to use
Sans Serif

Colors

Designer to choose colors to be used in the design.

Requirements
Must have
• Front of box must make it clear that it is instant coffee and show contents - 7 pack / 21g net as well as Drift Willow Roasters Co. which is the company name. We'd prefer the instant coffee be the focal point rather than the company name. The rear will have 'ingredients', company address and barcode. Sides should either state contents such as 'Instant Coffee' or company name.
Nice to have
• modern colour scheme - 'Drift Willow Roasters Co.' in a simple sans serif font
Should not have
• Must not be too 'busy' or 'cheap' looking

```html
<!DOCTYPE html>
<html lang="en">
<head>
<meta charset="UTF-8">
<title>Drift Willow Roasters Co. – Instant Coffee Pack</title>
<link rel="stylesheet" href="https://fonts.googleapis.com/css2?family=Oswald:wght@400;500;600&family=Bebas+Neue&display=swap">
<style>
  :root {
    --stage: #8c8c8c;
    --paper: #ffffff;
    --paper-shade: #eeeeee;
    --brown: #6b3a1f;
    --brown-deep: #4a2914;
    --bean-light: #a8693b;
    --cream: #f3e6d8;
    --lemon: #f2c21b;
  }
  * { margin: 0; padding: 0; box-sizing: border-box; }
  html, body { width: 1200px; height: 800px; overflow: hidden; }
  body {
    background: var(--stage);
    font-family: "Oswald", "Arial Narrow", sans-serif;
    color: var(--brown);
    position: relative;
  }
  .panel {
    position: absolute;
    background: var(--paper);
    text-align: center;
  }
  .front { left: 150px; top: 60px; width: 440px; height: 680px; }
  .side  { left: 610px; top: 60px; width: 200px; height: 680px; }
  .end   { left: 830px; top: 60px; width: 220px; height: 300px; }

  .company {
    font-family: "Bebas Neue", "Oswald", sans-serif;
    font-size: 26px;
    letter-spacing: 1px;
    color: var(--brown-deep);
  }
  .product-main {
    font-family: "Bebas Neue", "Oswald", sans-serif;
    font-size: 92px;
    line-height: .9;
    color: var(--brown-deep);
  }
  .product-sub {
    font-family: "Bebas Neue", "Oswald", sans-serif;
    font-size: 52px;
    line-height: .9;
    color: var(--brown-deep);
  }
  .front .company { margin-top: 48px; }
  .front .product-main { margin-top: 22px; }

  .cup-photo {
    width: 240px; height: 190px;
    margin: 26px auto 0;
    border-radius: 20px 20px 90px 90px;
    background: radial-gradient(circle at 55% 40%, var(--bean-light), var(--brown-deep) 75%);
  }

  .info-label { position: relative; width: 360px; height: 110px; margin: 18px auto 0; color: var(--cream); }
  .info-label svg { position: absolute; inset: 0; }
  .info-grid {
    position: absolute; inset: 8px 16px;
    display: grid; grid-template-columns: 1fr 110px;
    border: 1px solid var(--cream);
    text-align: left;
  }
  .info-main { border-right: 1px solid var(--cream); }
  .info-head {
    font-size: 11px; font-weight: 500; text-align: center;
    border-bottom: 1px solid var(--cream); padding: 3px 0;
  }
  .flavor { font-size: 11px; font-weight: 600; color: var(--lemon); padding: 3px 6px 0; }
  .directions { font-size: 10px; line-height: 1.35; padding: 2px 6px; }
  .brewed { font-size: 10px; font-weight: 500; padding: 22px 8px 0; }

  .net { margin-top: 22px; font-size: 20px; font-weight: 600; letter-spacing: 1px; color: var(--brown-deep); }

  .side .info-label { position: absolute; left: -80px; top: 285px; transform: rotate(-90deg); }

  .end { padding-top: 70px; }
  .end .company { font-size: 22px; }
  .end .product-main { font-size: 62px; margin-top: 10px; }
  .end .product-sub { font-size: 36px; }
</style>
</head>
<body>

<section class="panel front">
  <p class="company">Drift Willow Roasters Co.</p>
  <h1 class="product-main">Instant</h1>
  <p class="product-sub">Coffee</p>
  <div class="cup-photo" role="img" aria-label="Coffee cup shaped from roasted coffee beans"></div>
  <div class="info-label">
    <svg width="360" height="110" viewBox="0 0 360 110" aria-hidden="true">
      <path fill="var(--brown)" d="M5 0 H355 l5 5 -5 5 5 5 -5 5 5 5 -5 5 5 5 -5 5 5 5 -5 5 5 5 -5 5 5 5 -5 5 5 5 -5 5 5 5 -5 5 5 5 -5 5 5 5 -5 5 H5 l-5 -5 5 -5 -5 -5 5 -5 -5 -5 5 -5 -5 -5 5 -5 -5 -5 5 -5 -5 -5 5 -5 -5 -5 5 -5 -5 -5 5 -5 -5 -5 5 -5 -5 -5 5 -5 -5 -5 5 -5 Z"/>
    </svg>
    <div class="info-grid">
      <div class="info-main">
        <p class="info-head">100% PURE COFFEE</p>
        <p class="flavor">LEMON FLAVOR</p>
        <p class="directions">Soluble coffee. Add to Milk or Water. Add Sugar as per taste. Drink Hot or Cold.</p>
      </div>
      <p class="brewed">Brewed By:</p>
    </div>
  </div>
  <p class="net">7 PACK / 21G NET</p>
</section>

<section class="panel side">
  <div class="info-label">
    <svg width="360" height="110" viewBox="0 0 360 110" aria-hidden="true">
      <path fill="var(--brown)" d="M5 0 H355 l5 5 -5 5 5 5 -5 5 5 5 -5 5 5 5 -5 5 5 5 -5 5 5 5 -5 5 5 5 -5 5 5 5 -5 5 5 5 -5 5 5 5 -5 5 5 5 -5 5 H5 l-5 -5 5 -5 -5 -5 5 -5 -5 -5 5 -5 -5 -5 5 -5 -5 -5 5 -5 -5 -5 5 -5 -5 -5 5 -5 -5 -5 5 -5 -5 -5 5 -5 -5 -5 5 -5 -5 -5 5 -5 Z"/>
    </svg>
    <div class="info-grid">
      <div class="info-main">
        <p class="info-head">100% PURE COFFEE</p>
        <p class="flavor">LEMON FLAVOR</p>
        <p class="directions">Soluble coffee. Add to Milk or Water. Add Sugar as per taste. Drink Hot or Cold.</p>
      </div>
      <p class="brewed">Brewed By:</p>
    </div>
  </div>
</section>

<section class="panel end">
  <p class="company">Drift Willow Roasters Co.</p>
  <p class="product-main">Instant</p>
  <p class="product-sub">Coffee</p>
</section>

</body>
</html>
```